Business cards for property management company

Need new business cards designed for our property management company and rental community, Amber Knoll Commons. These cards will be primarily picked up by rental applicants.

May be single or double sided design.

I need cards for two different people, listed below. The design can be the same for both, and the only information that will be different is name and email address.

Industry/Entity Type

Property Management

Requirements
Must have
• US standard business card - 2''x3.5'' horizontal design.

1. Logo (attached). The text does not have to stay below the logo, but the card does need to say "Amber Knoll Commons" somewhere on it (does not have to be same font as logo, but those fonts are Americana Extra Bold and BlackJack if needed).
2. Name: one with "Lena Halvorsen" and one with "Dorian Halvorsen"
3. Email address: one with "lena@amberknollhub.com" and one with "dorian@amberknollhub.com"
4. Web address: amberknollhub.com
5. Phone: 281.555.0182
6. Address: 7390 Whitlock Avenue, Dickinson, Texas 77512 (zip code may me omitted, at your discretion)
Should not have
• No rounded corners or special cuts.

No bevel, emboss or shadow effects.

As a note, please do not use our website as a basis for color or design schemes. We are working on a redesign, based around the new logo (attached to brief).

```html
<!DOCTYPE html>
<html lang="en">
<head>
<meta charset="utf-8">
<title>Amber Knoll Commons – Business Cards</title>
<link href="https://fonts.googleapis.com/css2?family=Arimo:wght@400;700&family=Felipa&display=swap" rel="stylesheet">
<style>
  :root {
    --backdrop: #1c1c1e;
    --card: #ffffff;
    --teal: #2f93aa;
    --green: #5b8d2f;
    --frame: #7fbccb;
  }
  * { box-sizing: border-box; margin: 0; padding: 0; }
  html, body { width: 1200px; height: 783px; overflow: hidden; }
  body { background: var(--backdrop); position: relative; font-family: "Arimo", Arial, sans-serif; }

  .card {
    position: absolute;
    width: 530px;
    height: 296px;
    background: var(--card);
  }
  .card--lena { left: 150px; top: 138px; }
  .card--dorian { left: 455px; top: 362px; }

  .card__frame {
    position: absolute;
    inset: 9px;
    border: 1px solid var(--frame);
  }
  .card__frame::after {
    content: "";
    position: absolute;
    inset: 3px;
    border: 1px solid var(--frame);
  }

  .card__divider {
    position: absolute;
    left: 212px;
    top: 28px;
    bottom: 42px;
    width: 1.5px;
    background: var(--teal);
  }

  .brand {
    position: absolute;
    left: 24px;
    top: 60px;
    width: 176px;
    text-align: center;
    color: var(--green);
    font-weight: 700;
    font-size: 22px;
    line-height: 1.15;
  }
  .brand__dot {
    display: block;
    width: 64px;
    height: 64px;
    margin: 0 auto 14px;
    border-radius: 50%;
    background: var(--green);
  }

  .contact {
    position: absolute;
    left: 232px;
    top: 66px;
  }
  .contact__name {
    font-family: "Felipa", "Monotype Corsiva", cursive;
    font-size: 29px;
    color: var(--teal);
    line-height: 1;
    font-weight: 400;
  }
  .contact__email {
    font-size: 12px;
    color: var(--teal);
    margin-top: 2px;
  }
  .contact__web {
    font-size: 12px;
    color: var(--green);
    margin-top: 20px;
  }
  .contact__phone {
    font-size: 12px;
    font-weight: 700;
    color: var(--green);
    margin-top: 3px;
  }
  .contact__address {
    font-style: normal;
    font-size: 12px;
    line-height: 1.4;
    color: var(--green);
    margin-top: 22px;
  }
</style>
</head>
<body>

  <section class="card card--lena">
    <div class="card__frame"></div>
    <div class="brand"><span class="brand__dot"></span>Amber Knoll<br>Commons</div>
    <div class="card__divider"></div>
    <div class="contact">
      <h2 class="contact__name">Lena Halvorsen</h2>
      <p class="contact__email">lena@amberknollhub.com</p>
      <p class="contact__web">amberknollhub.com</p>
      <p class="contact__phone">281.555.0182</p>
      <address class="contact__address">7390 Whitlock Avenue<br>Dickinson, Texas 77512</address>
    </div>
  </section>

  <section class="card card--dorian">
    <div class="card__frame"></div>
    <div class="brand"><span class="brand__dot"></span>Amber Knoll<br>Commons</div>
    <div class="card__divider"></div>
    <div class="contact">
      <h2 class="contact__name">Dorian Halvorsen</h2>
      <p class="contact__email">dorian@amberknollhub.com</p>
      <p class="contact__web">amberknollhub.com</p>
      <p class="contact__phone">281.555.0182</p>
      <address class="contact__address">7390 Whitlock Avenue<br>Dickinson, Texas 77512</address>
    </div>
  </section>

</body>
</html>
```